Lucky Orbit Fun Casino Entertainment

Looking to update my business card and make it look more modern, stand out and eye catching.
We are are fun casino business in Australia (primarily Sydney). Blackjack and Roulette are our most popular games although we have pretty much every game available for hire that you would find in a real casino. The final design would need to be sleek and appeal to the more upmarket corporate sector.
We mainly cater for Corporate Events, Private Parties, Fundraising Events, Team Building, Poker Tournaments
I think I'd prefer the colour Black.

Target Market(s)

High-end Corporate

Industry/Entity Type

Events

Contact Information for Business Card

Dale Hutchins
Director
1300 482 617
0431 758 209
info@luckyorbit.com.au
www.luckyorbit.com.au
Facebook & Instagram @luckyorbitshows (proper social icons preferred)

Colors
000000
0255a3

Requirements
Must have
• Front side:
• Logo
• Contact details
• 'Australia's #1 Fun Casino Specialists'
• Back:
• Logo
Nice to have
• Back:
• Corporate Events
• Private Parties
• Poker Tournaments
• Fundraising
• Props & Theming
• Photo Booth
• Horse Racing Events
• The Vegas Sign attached, maybe on the back of the card in the background...?

```html
<!DOCTYPE html>
<html lang="en">
<head>
<meta charset="utf-8">
<title>Lucky Orbit Business Card</title>
<link href="https://fonts.googleapis.com/css2?family=Roboto:wght@400;700&display=swap" rel="stylesheet">
<style>
  :root {
    --stage: #efefef;
    --card: #000000;
    --gold: #f5a51c;
    --chip: #3a3a3c;
    --white: #ffffff;
  }
  html, body { margin: 0; padding: 0; overflow: hidden; }
  body {
    width: 1200px; height: 1000px;
    background: var(--stage);
    position: relative;
    font-family: 'Roboto', Arial, sans-serif;
  }
  .card-slot { position: absolute; overflow: hidden; box-shadow: 0 0 2px rgba(0,0,0,.25); }
  .card-slot.large { width: 468px; height: 274px; }
  .card-slot.small { width: 262px; height: 153px; }
  .card {
    position: absolute; left: 0; top: 0;
    width: 468px; height: 274px;
    background: var(--card); color: var(--white);
    transform-origin: 0 0;
  }
  .small .card { transform: scale(0.56); }

  .brand-disc { position: absolute; border-radius: 50%; background: var(--chip); border: 5px solid var(--gold); box-sizing: border-box; }
  .brand-name { position: absolute; color: var(--gold); font-weight: 700; text-transform: uppercase; line-height: 1; letter-spacing: .5px; white-space: nowrap; }

  .front .brand-disc { left: 30px; top: 60px; width: 100px; height: 100px; }
  .front .brand-name { left: 142px; top: 84px; font-size: 26px; }

  .person { position: absolute; left: 262px; top: 99px; width: 158px; text-align: center; }
  .person-name { color: var(--gold); font-size: 19px; font-weight: 400; white-space: nowrap; padding-bottom: 4px; border-bottom: 1px solid var(--gold); }
  .person-role { font-size: 11px; letter-spacing: 4.5px; margin-top: 6px; padding-left: 4px; }

  .tagline { position: absolute; left: 184px; top: 192px; font-size: 12px; }
  .contacts { position: absolute; left: 184px; top: 215px; display: grid; grid-template-columns: 142px 140px; row-gap: 4px; font-size: 9px; }
  .contact { display: flex; align-items: center; gap: 6px; height: 11px; white-space: nowrap; }
  .contact svg { width: 10px; height: 10px; flex: none; }

  .back .brand-disc { left: 108px; top: 76px; width: 92px; height: 92px; }
  .back .brand-name { left: 212px; top: 109px; font-size: 26px; }
  .services { position: absolute; left: 0; right: 0; top: 218px; text-align: center; font-size: 11px; line-height: 18px; }
  .services .dot { margin: 0 6px; }
</style>
</head>
<body>

<div class="card-slot large" style="left:108px; top:316px;">
  <div class="card front">
    <div class="brand-disc"></div>
    <div class="brand-name">Lucky<br>Orbit</div>
    <div class="person">
      <div class="person-name">DALE HUTCHINS</div>
      <div class="person-role">DIRECTOR</div>
    </div>
    <div class="tagline">Australia's #1 Fun Casino Specialists</div>
    <div class="contacts">
      <div class="contact"><svg viewBox="0 0 10 10"><rect width="10" height="10" rx="2" fill="#f5a51c"/><path d="M3 2.3l1.2 1.3-.6.8c.4.8 1 1.4 1.9 1.9l.8-.6 1.4 1.2-.7 1C4.6 7.6 2.5 5.5 2.2 3z" fill="#000"/></svg>1300 482 617</div>
      <div class="contact"><svg viewBox="0 0 10 10"><rect width="10" height="10" rx="2" fill="#f5a51c"/><circle cx="5" cy="5" r="3" fill="none" stroke="#000" stroke-width=".8"/><path d="M2 5h6M5 2v6" stroke="#000" stroke-width=".6"/></svg>www.luckyorbit.com.au</div>
      <div class="contact"><svg viewBox="0 0 10 10"><rect width="10" height="10" rx="2" fill="#f5a51c"/><path d="M3 2.3l1.2 1.3-.6.8c.4.8 1 1.4 1.9 1.9l.8-.6 1.4 1.2-.7 1C4.6 7.6 2.5 5.5 2.2 3z" fill="#000"/></svg>0431 758 209</div>
      <div class="contact"><svg viewBox="0 0 10 10"><rect width="10" height="10" rx="2" fill="#f5a51c"/></svg>@luckyorbitshows</div>
      <div class="contact"><svg viewBox="0 0 10 10"><rect width="10" height="10" rx="2" fill="#f5a51c"/><rect x="2.2" y="3" width="5.6" height="4" fill="#000"/><path d="M2.4 3.2L5 5.2l2.6-2" fill="none" stroke="#f5a51c" stroke-width=".6"/></svg>info@luckyorbit.com.au</div>
      <div class="contact"><svg viewBox="0 0 10 10"><rect width="10" height="10" rx="2" fill="#f5a51c"/></svg>@luckyorbitshows</div>
    </div>
  </div>
</div>

<div class="card-slot large" style="left:624px; top:316px;">
  <div class="card back">
    <div class="brand-disc"></div>
    <div class="brand-name">Lucky Orbit</div>
    <div class="services">
      <div>Corporate Events<span class="dot">•</span>Private Parties<span class="dot">•</span>Poker Tournaments<span class="dot">•</span>Fundraising</div>
      <div>Props &amp; Theming<span class="dot">•</span>Photo Booth<span class="dot">•</span>Horse Racing Events</div>
    </div>
  </div>
</div>

<div class="card-slot small" style="left:324px; top:796px;">
  <div class="card front">
    <div class="brand-disc"></div>
    <div class="brand-name">Lucky<br>Orbit</div>
    <div class="person">
      <div class="person-name">DALE HUTCHINS</div>
      <div class="person-role">DIRECTOR</div>
    </div>
    <div class="tagline">Australia's #1 Fun Casino Specialists</div>
    <div class="contacts">
      <div class="contact"><svg viewBox="0 0 10 10"><rect width="10" height="10" rx="2" fill="#f5a51c"/></svg>1300 482 617</div>
      <div class="contact"><svg viewBox="0 0 10 10"><rect width="10" height="10" rx="2" fill="#f5a51c"/></svg>www.luckyorbit.com.au</div>
      <div class="contact"><svg viewBox="0 0 10 10"><rect width="10" height="10" rx="2" fill="#f5a51c"/></svg>0431 758 209</div>
      <div class="contact"><svg viewBox="0 0 10 10"><rect width="10" height="10" rx="2" fill="#f5a51c"/></svg>@luckyorbitshows</div>
      <div class="contact"><svg viewBox="0 0 10 10"><rect width="10" height="10" rx="2" fill="#f5a51c"/></svg>info@luckyorbit.com.au</div>
      <div class="contact"><svg viewBox="0 0 10 10"><rect width="10" height="10" rx="2" fill="#f5a51c"/></svg>@luckyorbitshows</div>
    </div>
  </div>
</div>

<div class="card-slot small" style="left:614px; top:796px;">
  <div class="card back">
    <div class="brand-disc"></div>
    <div class="brand-name">Lucky Orbit</div>
    <div class="services">
      <div>Corporate Events<span class="dot">•</span>Private Parties<span class="dot">•</span>Poker Tournaments<span class="dot">•</span>Fundraising</div>
      <div>Props &amp; Theming<span class="dot">•</span>Photo Booth<span class="dot">•</span>Horse Racing Events</div>
    </div>
  </div>
</div>

</body>
</html>
```